Birchway Swing Studio New Location Postcard

I need a postcard announcing our new location. It is a indoor golf training facility that offers award winner instruction, state-of-the-art technology, and custom club fitting. Whether you are a beginner, an aspiring athlete, or an amateur, Birchway Swing Studio offers personalized programs to help take your game to the next level. Call now to schedule your free tour or to sign up. Limited memberships available.
I would like somewhere are on postcard to say Don't put away your clubs just yet! The course may be closed but Birchway Swing Studio's new indoor location is open!
Industry/Entity Type
Training
Look and feel
Each slider illustrates characteristics of the customer's brand and the style your logo design should communicate.

```html
<!DOCTYPE html>
<html lang="en">
<head>
<meta charset="utf-8">
<title>Birchway Swing Studio – New Location Postcard</title>
<link href="https://fonts.googleapis.com/css2?family=Lato:wght@300;400;700;900&display=swap" rel="stylesheet">
<style>
  :root{
    --red:#e8453c;
    --black:#111;
    --white:#fff;
    --page:#9a9a9a;
  }
  *{margin:0;padding:0;box-sizing:border-box}
  html,body{width:1200px;height:1200px;overflow:hidden}
  body{background:var(--page);font-family:'Lato',sans-serif;color:var(--white);position:relative}
  .card{position:absolute;left:264px;width:670px;height:520px;overflow:hidden;box-shadow:0 4px 14px rgba(0,0,0,.35)}
  .card--front{top:52px}
  .card--back{top:628px;background:var(--white)}
  .card svg.bg{position:absolute;inset:0}
  .abs{position:absolute;white-space:nowrap}

  /* front */
  .kicker{left:16px;top:190px;font-size:18px;font-weight:700;letter-spacing:-.2px;text-shadow:0 1px 3px rgba(0,0,0,.5)}
  .headline{left:12px;top:206px;font-size:78px;font-weight:900;letter-spacing:-2px;text-shadow:0 2px 6px rgba(0,0,0,.5)}
  .brand{display:flex;align-items:center;gap:8px}
  .brand__dot{width:22px;height:22px;border:2px solid var(--white);border-radius:50%;flex:none}
  .brand__name{font-weight:300;text-transform:uppercase}
  .front-brand{right:18px;top:336px}
  .front-brand .brand__name{font-size:20px}
  .front-tag{right:20px;top:362px;font-size:9px;font-weight:400;letter-spacing:.3px}
  .cta{right:16px;top:371px;font-size:34px;font-weight:900}
  .cta-sub{right:16px;top:412px;font-size:14px;font-weight:400}
  .front-phone{right:18px;top:430px;font-size:40px;font-weight:900}
  .front-web{right:16px;top:479px;font-size:21px;font-weight:400}
  .about{position:absolute;left:16px;top:372px;width:344px;font-size:14px;line-height:18px;font-weight:300;text-align:justify}
  .limited{left:16px;top:484px;font-size:18px;font-weight:700}

  /* back */
  .back-dot{left:128px;top:26px;width:68px;height:68px;border:3px solid var(--white);border-radius:50%}
  .back-brand{left:0;width:324px;top:110px;text-align:center;font-size:21px;font-weight:300;text-transform:uppercase}
  .back-tag{left:0;width:324px;top:144px;text-align:center;font-size:11px;letter-spacing:.3px}
  .pitch{position:absolute;left:16px;top:185px;width:298px}
  .pitch__a{font-size:18px;font-weight:700;line-height:23px}
  .pitch__b{font-size:18px;font-weight:700;line-height:23px;text-align:justify;text-align-last:justify}
  .pitch__c{font-size:17px;font-weight:400;line-height:30px;white-space:nowrap}
  .pitch__d{font-size:29px;font-weight:900;line-height:36px}
  .contact{position:absolute;left:16px;display:flex;align-items:center;gap:20px}
  .contact svg{width:20px;height:22px;flex:none}
  .contact--phone{top:320px;font-size:30px;font-weight:900}
  .contact--web{top:364px;font-size:19px}
  .contact--mail{top:398px;font-size:19px}
  .contact--addr{top:434px;font-size:19px;align-items:flex-start;line-height:24px}
  .stamp{position:absolute;left:578px;top:18px;width:76px;height:76px;border:2px solid var(--black)}
  .addr-line{position:absolute;left:438px;width:216px;height:1.5px;background:var(--black)}
</style>
</head>
<body>

<section class="card card--front">
  <svg class="bg" viewBox="0 0 670 520" width="670" height="520">
    <defs>
      <linearGradient id="facility" x1="0" y1="0" x2="0" y2="1">
        <stop offset="0" stop-color="#c9c8c0"/>
        <stop offset=".3" stop-color="#3b4fa6"/>
        <stop offset=".5" stop-color="#5a6472"/>
        <stop offset=".7" stop-color="#4f7a3a"/>
        <stop offset="1" stop-color="#3f6a2e"/>
      </linearGradient>
    </defs>
    <rect width="670" height="360" fill="url(#facility)" role="img" aria-label="Photo of the indoor golf training bays with hitting nets, turf mats and a putting green"/>
    <path d="M0 300 C170 336 380 304 670 246" fill="none" stroke="var(--red)" stroke-width="2"/>
    <path d="M0 312 C170 348 380 316 670 258 L670 520 L0 520Z" fill="var(--black)"/>
    <path d="M0 324 C170 360 380 328 670 270 L670 520 L0 520Z" fill="var(--white)"/>
    <path d="M0 336 C170 372 380 340 670 282 L670 520 L0 520Z" fill="var(--red)"/>
  </svg>
  <div class="abs kicker">NEW INDOOR LOCATION IS</div>
  <div class="abs headline">OPEN!</div>

  <div class="abs brand front-brand"><span class="brand__dot"></span><span class="brand__name">Birchway Swing Studio</span></div>
  <div class="abs front-tag">PRACTICE. IMPROVE. BE BETTER</div>
  <div class="abs cta">CALL NOW</div>
  <div class="abs cta-sub">to schedule your free tour or to sign up</div>
  <div class="abs front-phone">555-014-2290</div>
  <div class="abs front-web">www.birchwayswing.com</div>

  <p class="about">It is a indoor golf training facility that offers award winner instruction, state-of-the-art technology, and custom club fitting. Whether you are a beginner, an aspiring athlete, or an amateur, Birchway Swing Studio offers personalized programs to help take your game to the next level.</p>
  <div class="abs limited">LIMITED MEMBERSHIPS AVAILABLE</div>
</section>

<section class="card card--back">
  <svg class="bg" viewBox="0 0 670 520" width="670" height="520">
    <defs>
      <linearGradient id="lesson" x1="0" y1="0" x2="0" y2="1">
        <stop offset="0" stop-color="#8a94a0"/>
        <stop offset=".35" stop-color="#3e5a34"/>
        <stop offset="1" stop-color="#2c4425"/>
      </linearGradient>
    </defs>
    <path d="M0 0 L386 0 C354 100 336 200 348 290 C358 360 386 430 398 520 L0 520Z" fill="var(--red)"/>
    <path d="M0 0 L383 0 C351 100 333 200 345 290 C355 360 383 430 395 520 L0 520Z" fill="var(--white)"/>
    <path d="M0 0 L378 0 C346 100 328 200 340 290 C350 360 378 430 390 520 L0 520Z" fill="var(--black)"/>
    <path d="M0 0 L372 0 C340 100 322 200 334 290 C344 360 372 430 384 520 L0 520Z" fill="var(--white)"/>
    <path d="M0 0 L366 0 C334 100 316 200 328 290 C338 360 366 430 378 520 L0 520Z" fill="var(--red)"/>
    <circle cx="380" cy="418" r="90" fill="none" stroke="var(--red)" stroke-width="3"/>
    <circle cx="380" cy="418" r="86" fill="url(#lesson)" stroke="var(--black)" stroke-width="4" role="img" aria-label="Photo of a young golfer practicing putting on indoor turf with a coach"/>
  </svg>

  <div class="abs back-dot"></div>
  <div class="abs back-brand">Birchway Swing Studio</div>
  <div class="abs back-tag">PRACTICE. IMPROVE. BE BETTER</div>

  <div class="pitch">
    <div class="pitch__a">Don't put away your clubs just yet!</div>
    <div class="pitch__b">The course may be closed but</div>
    <div class="pitch__c">Birchway Swing Studio's new indoor</div>
    <div class="pitch__d">LOCATION IS OPEN!</div>
  </div>

  <div class="contact contact--phone">
    <svg viewBox="0 0 20 22"><path d="M9 2 C3 4 3 18 9 20 L10 16 C7 15 7 7 10 6Z" fill="var(--white)"/></svg>
    <span>555-014-2290</span>
  </div>
  <div class="contact contact--web">
    <svg viewBox="0 0 20 22"><rect x="1" y="6" width="18" height="11" fill="none" stroke="var(--white)" stroke-width="1.6"/><path d="M1 6 L10 13 L19 6 M1 17 L8 11 M19 17 L12 11" fill="none" stroke="var(--white)" stroke-width="1.4"/></svg>
    <span>www.birchwayswing.com</span>
  </div>
  <div class="contact contact--mail">
    <svg viewBox="0 0 20 22"><circle cx="10" cy="11" r="8.5" fill="none" stroke="var(--white)" stroke-width="1.5"/><ellipse cx="10" cy="11" rx="4" ry="8.5" fill="none" stroke="var(--white)" stroke-width="1.2"/><path d="M1.5 11 H18.5 M3 6.5 H17 M3 15.5 H17" stroke="var(--white)" stroke-width="1.2"/></svg>
    <span>info@birchwayswing.com</span>
  </div>
  <div class="contact contact--addr">
    <svg viewBox="0 0 20 22"><path d="M10 21 C4 13 3 10 3 8 A7 7 0 0 1 17 8 C17 10 16 13 10 21Z" fill="var(--white)"/><circle cx="10" cy="8" r="2.6" fill="var(--red)"/></svg>
    <span>Birchway Swing Studio Inc.<br>4810 Alder Park Rd. Unit B3<br>Maple Falls, OH 45999</span>
  </div>

  <div class="stamp"></div>
  <div class="addr-line" style="top:286px"></div>
  <div class="addr-line" style="top:306px"></div>
  <div class="addr-line" style="top:326px"></div>
</section>

</body>
</html>
```